Contemporary Elegant Business Card Design for an International Trade Company in the Wine Industry

We need a new business card design for an international trade company in the wine and winemaking industry. The overall feel of the card should be contemporary, upscale, luxurious and elegant. It should communicate confidence and professionalism. The colors should complementary to our logo design (burgundy, gold, and black).
Inspiration: rich velvet tapestry
The card should include the following information:
Business: Brovenna Trading/Shipping, LLC.
Name: Marcus T. Hollenbrand
Title: CEO
Email: mark@brovennatrading.example
Phone: 555-294-6172
www.brovennatrading.example
Updates
Project Deadline Extended
Reason: We'd like the designers that we requested some additional designs from to still submit designs. Thank you!
Industry/Entity Type
Business
Contact Information for Business Card
Title: CEO
Phone: 555-294-6172
www.brovennatrading.example
Look and feel

```html
<!DOCTYPE html>
<html lang="en">
<head>
<meta charset="utf-8">
<title>Brovenna Trading/Shipping, LLC. — Business Card Front</title>
<link rel="stylesheet" href="https://fonts.googleapis.com/css2?family=Marcellus&display=swap">
<style>
  :root {
    --burgundy: #6e111a;
    --gold: #e3b251;
    --paper: #ffffff;
    --frame: #1a1a1a;
  }
  * { margin: 0; padding: 0; box-sizing: border-box; }
  html, body {
    width: 1200px;
    height: 686px;
    overflow: hidden;
    background: var(--paper);
  }
  .card {
    position: relative;
    width: 1200px;
    height: 686px;
    background: var(--paper);
    border: 1px solid var(--frame);
    overflow: hidden;
  }
  .brand-mark {
    position: absolute;
    left: 50%;
    top: 182px;
    width: 150px;
    height: 150px;
    margin-left: -75px;
    border-radius: 50%;
    background: var(--burgundy);
  }
  .brand-name {
    position: absolute;
    left: 0;
    right: 0;
    top: 378px;
    text-align: center;
    font-family: "Marcellus", "Times New Roman", serif;
    font-weight: 400;
    color: var(--gold);
    text-transform: uppercase;
  }
  .brand-name__main {
    display: block;
    font-size: 88px;
    line-height: 1;
    letter-spacing: 6px;
  }
  .brand-name__sub {
    display: block;
    margin-top: 18px;
    font-size: 33px;
    line-height: 1;
    letter-spacing: 6px;
  }
  .footer-band {
    position: absolute;
    left: 0;
    bottom: 0;
    width: 1200px;
    height: 48px;
    display: block;
  }
</style>
</head>
<body>
  <main class="card">
    <div class="brand-mark" aria-hidden="true"></div>
    <h1 class="brand-name">
      <span class="brand-name__main">Brovenna</span>
      <span class="brand-name__sub">Trading/Shipping, LLC.</span>
    </h1>
    <svg class="footer-band" viewBox="0 0 1200 48" aria-hidden="true">
      <rect x="0" y="0" width="1200" height="48" fill="var(--burgundy)"/>
      <polygon points="898,0 912,0 890,48 876,48" fill="var(--paper)"/>
    </svg>
  </main>
</body>
</html>
```